Brisk Mend's Blow Their Mind Website

We own a group of cell phone and tablet repair shops in the bay area that is emerging into the mobile device insurance industry and want to develop a site that is clean, organized, and efficient at communicating who we are, the services we provide and the positive feedback we have been getting from our clients. As we enter into this new field of business, Our goal is to attract larger corporate accounts.

We want our home screen to have a big focus on the protection plan for the devices right away much like the home screen from these links:

http://www.gadgetvault.com/

and also - https://us.keepitsnug.com/smartphone-protection.html

We also need to make our repair services clear, here is a website of a company that does repair and we want to highlight both ends of the business.

ww.fixnovo.com

So the home screen will include the tab categories at the top of the screen
home/ protection /repair /about /contact

The first portion will be protection and as you scroll down there will be the next section about repair and following that will be information about the company.

Target Market(s)

Individuals that would be looking for pricing, clients that come to our store, but ultimately the heavy hitters we would want to attract would be larger corporate accounts so the message we want to communicate is professional, organized and credible in the services we provide.

Industry/Entity Type

Cell Phone

Number of Pages Required

5+ page

Font styles to use
Serif

Colors
34a6d7

Requirements
Must have
• Eye catching, organized, with the wow factor that a business will look at our site and will be able to tell that we know what looks good and what grabs peoples attention. A large emphasis on the protection plan section like the links we provided and an organized home screen with the sections highlighted in the project description
• Tabs with links to different sections of the business such as protection that will go into detail about our protections plans and why our plan is best
• repair with a menu of the different prices we provide for different devices and services for that device
• an about us tab
• a contact us tab
Nice to have
• Artistic flow on the homescreen that the different sections flow together without looking too cookie cutter
• Wow factor
Should not have
• Clutter, confusion, disorganization, cheesy cookie cutter

```html
<!DOCTYPE html>
<html lang="en">
<head>
<meta charset="utf-8">
<title>Brisk Mend</title>
<link rel="stylesheet" href="https://fonts.googleapis.com/css2?family=Open+Sans:wght@300;400;600;700&display=swap">
<style>
:root{
  --brand:#34a6d7;
  --brand-dark:#1f6f8c;
  --band:#2a7fa0;
  --ink:#333;
  --muted:#777;
  --footer:#e9e9e9;
  --footer-bar:#dcdcdc;
  --star:#f2b01e;
  --white:#fff;
}
*{box-sizing:border-box;margin:0;padding:0}
html,body{width:736px;height:1200px;overflow:hidden}
body{font-family:"Open Sans",sans-serif;color:var(--ink);background:var(--white);position:relative}
.site-header{position:absolute;top:0;left:0;width:736px;height:36px;display:flex;align-items:center;padding:0 60px 0 96px;background:var(--white)}
.brand{display:flex;align-items:center;gap:6px;font-size:15px;font-weight:600;color:var(--brand)}
.brand-dot{width:12px;height:12px;border-radius:50%;background:var(--brand)}
.main-nav{margin-left:auto;display:flex;gap:14px;font-size:6.5px;font-weight:700;color:var(--ink)}
.main-nav .active{color:var(--brand)}
.header-tools{display:flex;gap:14px;margin-left:30px}
.tool{display:flex;flex-direction:column;align-items:center;font-size:5.5px;color:var(--muted);gap:1px}
.hero{position:absolute;top:36px;left:0;width:736px;height:264px;background:linear-gradient(90deg,#f7fbfd 0%,#eef5f9 45%,#dde9f0 100%)}
.hero-photo{position:absolute;right:0;top:0;width:400px;height:264px;background:linear-gradient(120deg,#e9f1f6 0%,#b9c9d4 45%,#6f8594 70%,#d9e3ea 100%)}
.hero-copy{position:absolute;left:100px;top:66px;width:300px}
.hero-copy h1{font-size:22px;font-weight:400;color:var(--brand);margin-bottom:14px;white-space:nowrap}
.hero-copy p{font-size:6.5px;line-height:1.6;color:var(--muted);margin-bottom:18px;width:230px}
.btn{display:inline-block;background:var(--brand-dark);color:var(--white);font-size:6.5px;font-weight:600;padding:9px 24px;letter-spacing:.5px}
.reviews{position:absolute;top:284px;left:100px;width:536px;display:flex;justify-content:space-between}
.review{width:112px;height:112px;border-radius:50%;background:var(--white);border:1px solid #e3e3e3;box-shadow:0 2px 6px rgba(0,0,0,.08);display:flex;flex-direction:column;align-items:center;justify-content:center;text-align:center;padding:0 16px}
.stars{color:var(--star);font-size:12px;letter-spacing:1px;margin-bottom:4px}
.review p{font-size:4.5px;line-height:1.5;color:var(--muted);margin-bottom:4px}
.review a{font-size:6px;color:var(--brand-dark);text-decoration:none;font-weight:600}
.about-band{position:absolute;top:420px;left:0;width:736px;height:182px;background:var(--band)}
.about-copy{position:absolute;left:100px;top:24px;width:220px;color:var(--white)}
.about-copy h2{font-size:28px;font-weight:300;margin-bottom:12px}
.about-copy p{font-size:6.5px;line-height:1.6;margin-bottom:14px}
.btn-outline{display:inline-block;border:1px solid var(--white);color:var(--white);font-size:10px;padding:6px 14px}
.about-photo{position:absolute;right:96px;top:30px;width:226px;height:122px;background:linear-gradient(135deg,#f4f4f4 0%,#d9d9d9 60%,#b9b9b9 100%);border:3px solid var(--white)}
.repair{position:absolute;top:602px;left:0;width:736px;height:260px;background:var(--white)}
.repair-photo{position:absolute;left:100px;top:64px;width:120px;height:132px;background:linear-gradient(90deg,#cfd3d6 0%,#8e959a 45%,#2c2f33 55%,#3b4b5c 100%);border-radius:10px}
.repair-copy{position:absolute;left:250px;top:40px;width:390px}
.repair-copy h2{font-size:20px;font-weight:400;color:#555;margin-bottom:10px}
.repair-copy p{font-size:6.5px;line-height:1.6;color:var(--muted);margin-bottom:10px}
.press{position:absolute;top:866px;left:0;width:736px;text-align:center}
.press h3{font-size:18px;font-weight:400;color:#555;margin-bottom:22px}
.press-list{display:flex;justify-content:center;gap:42px;font-size:15px;font-weight:600;color:#9a9a9a}
.site-footer{position:absolute;top:978px;left:0;width:736px;height:222px;background:var(--footer)}
.footer-col{position:absolute;top:18px;font-size:6px;color:var(--muted)}
.footer-col h4{font-size:7px;font-weight:700;color:var(--ink);margin-bottom:12px}
.quick-links li{list-style:none;margin-bottom:6px}
.quick-links li::before{content:"› ";color:var(--brand)}
.testimonial{display:flex;gap:10px;width:200px;border-bottom:1px solid #ccc;padding-bottom:10px}
.avatar{width:32px;height:32px;background:linear-gradient(135deg,#e8c9b0,#b58b6c);flex:none}
.testimonial strong{display:block;color:var(--brand);font-size:6px;margin-bottom:3px}
.contact-line{display:flex;align-items:center;gap:6px;margin-bottom:8px}
.socials{display:flex;gap:5px;margin-top:4px}
.social{width:16px;height:16px;background:#d9534f}
.social.alt{background:var(--brand)}
.footer-bar{position:absolute;bottom:0;left:0;width:736px;height:26px;background:var(--footer-bar);font-size:6px;color:var(--muted);display:flex;align-items:center;justify-content:center}
</style>
</head>
<body>
<header class="site-header">
  <div class="brand"><span class="brand-dot"></span>Brisk Mend</div>
  <nav class="main-nav"><span class="active">HOME</span><span>PROTECTION</span><span>REPAIR</span><span>ABOUT</span><span>CONTACT</span></nav>
  <div class="header-tools">
    <div class="tool"><svg width="10" height="10" viewBox="0 0 10 10"><circle cx="4" cy="4" r="3" fill="none" stroke="#777" stroke-width="1"/><line x1="6.2" y1="6.2" x2="9" y2="9" stroke="#777" stroke-width="1"/></svg>Search</div>
    <div class="tool"><svg width="10" height="10" viewBox="0 0 10 10"><circle cx="5" cy="3" r="2.2" fill="none" stroke="#777"/><path d="M1 10c0-3 8-3 8 0" fill="none" stroke="#777"/></svg>Account</div>
  </div>
</header>

<section class="hero">
  <div class="hero-photo" role="img" aria-label="Hand holding a smartphone with a cracked screen"></div>
  <div class="hero-copy">
    <h1>Welcome To Brisk Mend</h1>
    <p>Protection plans that cover cracked screens, water damage and theft, backed by expert same-day repair for phones and tablets across the Bay Area.</p>
    <span class="btn">VIEW PROTECTION PLANS</span>
  </div>
</section>

<section class="reviews">
  <div class="review"><div class="stars">★★★★☆</div><p>Fast friendly service, my phone screen looks new again.</p><a>Lorem Ipsum</a></div>
  <div class="review"><div class="stars">★★★★☆</div><p>Great price and quick repair, back in one hour.</p><a>Lorem Ipsum</a></div>
  <div class="review"><div class="stars">★★★★☆</div><p>Helpful staff explained the protection plan very clearly.</p><a>Lorem Ipsum</a></div>
  <div class="review"><div class="stars">★★★★☆</div><p>Our whole office trusts them with every device.</p><a>Lorem Ipsum</a></div>
</section>

<section class="about-band">
  <div class="about-copy">
    <h2>Who we are?</h2>
    <p>A group of Bay Area repair shops now protecting devices for people and businesses, with clear pricing, quick claims and skilled technicians you can trust.</p>
    <span class="btn-outline">Read More</span>
  </div>
  <div class="about-photo" role="img" aria-label="Hands holding a smartphone playing a video"></div>
</section>

<section class="repair">
  <div class="repair-photo" role="img" aria-label="Two smartphones shown front and back"></div>
  <div class="repair-copy">
    <h2>Expert Repair For Every Device</h2>
    <p>Screens, batteries, charging ports, cameras and water damage fixed by certified technicians, most repairs finished the same day with genuine quality parts and a warranty on every job.</p>
    <p>See our full price menu for each phone and tablet model, or bring your device to any of our shops for a free diagnosis and honest quote.</p>
    <span class="btn">SEE REPAIR PRICES</span>
  </div>
</section>

<section class="press">
  <h3>Our Press</h3>
  <div class="press-list"><span>Northwind</span><span>Brightwave</span><span>Daylight</span><span>Coastline</span><span>Marketpost</span></div>
</section>

<footer class="site-footer">
  <div class="footer-col" style="left:100px">
    <h4>Quick Link</h4>
    <ul class="quick-links"><li>Home</li><li>Protection</li><li>Repair</li><li>About</li><li>Contact</li></ul>
  </div>
  <div class="footer-col" style="left:236px">
    <h4>Testimonials</h4>
    <div class="testimonial">
      <div class="avatar" role="img" aria-label="Customer portrait"></div>
      <div><strong>Dana Holt</strong>Quick repair and great price, highly recommend this team to anyone.</div>
    </div>
  </div>
  <div class="footer-col" style="left:490px">
    <h4>Contact Us</h4>
    <div class="contact-line"><svg width="8" height="8" viewBox="0 0 8 8"><path d="M1 1h2l1 2-1 1a4 4 0 0 0 2 2l1-1 2 1v2C3 8 0 5 1 1z" fill="#777"/></svg>(415) 555-0148</div>
    <div class="contact-line"><svg width="8" height="8" viewBox="0 0 8 8"><rect x="0.5" y="1.5" width="7" height="5" fill="none" stroke="#777"/><path d="M0.5 1.5l3.5 3 3.5-3" fill="none" stroke="#777"/></svg>hello@briskmend.com</div>
    <h4 style="margin-top:10px">Follow us</h4>
    <div class="socials"><span class="social"></span><span class="social alt"></span><span class="social alt"></span><span class="social"></span></div>
  </div>
  <div class="footer-bar">Copyright © 2015 Brisk Mend. All rights reserved.</div>
</footer>
</body>
</html>
```